Serene Spiritual Website Wanted for World Wide Organisation

We need a serene, clean web design for our organisation that works around the world.

What We Do
We aim to bring life into synergy across the world. We inspire, motivate, synchronise, and harmonise. We work with energy which is essential to all of life (environmental, human & animal). Our website must depict the spiritual element of being innately natural and reflect animism.

We have included a PDF attachment with details of the structure, navigation, and some websites for ideas/reference. The logo is also attached.
Updates

Target Market(s)

Anyone over 18yrs looking for answers to life's big questions or looking to develop themselves

Industry/Entity Type

Spiritual/wellbeing/Self Development

Number of Pages Required

5+ page

Requirements
Must have
• It must be serene and natural looking, it must incorporate the logo.
Nice to have
• We have included a Powerpoint document which may help you understand what we need, it is just an idea for structure and style, it is not set in stone so feel free to be as creative as you like!
Should not have
• Not clinical.

```html
<!DOCTYPE html>
<html lang="en">
<head>
<meta charset="utf-8">
<title>Harmonaura – Website Pages</title>
<link href="https://fonts.googleapis.com/css2?family=Poppins:wght@400;500;600;700&display=swap" rel="stylesheet">
<style>
:root{
  --navy:#2f2d62;
  --navy-soft:#6d6b9c;
  --gold:#c8b66a;
  --gold-soft:#ddd09a;
  --ink:#2b2b3a;
  --muted:#8b8b96;
  --canvas:#faf7e8;
  --mist:#f2f1f5;
  --cream:#f6f1df;
  --white:#ffffff;
}
*{box-sizing:border-box;margin:0;padding:0}
html,body{width:1200px;height:2541px;overflow:hidden}
body{background:var(--canvas);font-family:'Poppins',sans-serif;position:relative;color:var(--ink)}
.page{position:absolute;width:337px;background:var(--white);overflow:hidden;box-shadow:0 0 3px rgba(0,0,0,.14)}
.col-a{left:43px}.col-b{left:424px}.col-c{left:814px}

.topbar{position:absolute;top:0;left:0;right:0;height:9px;background:var(--navy);color:var(--white);font-size:3.6px;line-height:9px;text-align:right;padding-right:34px;z-index:4}
.nav{position:absolute;top:9px;left:0;right:0;height:25px;display:flex;justify-content:flex-end;align-items:center;gap:20px;padding-right:30px;font-size:3.8px;font-weight:500;color:var(--ink);z-index:4}
.brand{position:absolute;left:33px;top:3px;width:46px;height:46px;border-radius:50%;background:var(--navy);z-index:5;display:flex;align-items:center;justify-content:center}
.brand-name{font-size:5px;font-weight:600;color:var(--gold)}

.hero{position:absolute;top:34px;left:0;right:0}
.hero .ph{position:absolute;inset:0}
.hero h1{position:absolute;left:0;right:0;text-align:center;color:var(--white);font-weight:600;font-size:19px;z-index:2}
.hero .wave{position:absolute;left:0;bottom:-1px;width:100%;height:56px;z-index:1}

.sec{position:absolute;left:0;right:0}
.abs{position:absolute}
.title{font-size:8px;font-weight:600;color:var(--navy);text-align:center}
.title.left{text-align:left}
.title.light{color:var(--white)}
.txt{font-size:3.3px;line-height:5.2px;color:var(--muted)}
.txt.light{color:#f1eee6}
.center{text-align:center}
.head-sm{font-size:4.6px;line-height:6.4px;font-weight:600;color:var(--navy)}
.date{font-size:3.6px;color:var(--gold);font-weight:500;margin:3px 0}
.link{font-size:3.6px;font-weight:600;color:var(--navy);margin-top:4px}
.btn{display:inline-block;border-radius:8px;font-size:3.6px;font-weight:500;padding:2.5px 9px;color:var(--white);background:var(--gold)}
.btn.navy{background:var(--navy)}
.btn.line{background:var(--white);border:.6px solid var(--navy);color:var(--navy)}

.card{position:absolute;background:var(--white);border-radius:7px;box-shadow:0 1px 4px rgba(0,0,0,.16);overflow:hidden;text-align:center}
.frame{position:absolute;background:var(--white);border:1.5px solid var(--gold-soft);text-align:center;padding:3px}
.round{border-radius:50%}
.ring{border:4px solid var(--navy-soft)}
.ring-gold{border:2px solid var(--gold)}

.play{position:absolute;left:50%;top:50%;width:14px;height:14px;margin:-7px 0 0 -7px;border-radius:50%;border:1px solid var(--white);background:rgba(0,0,0,.3)}
.play::after{content:"";position:absolute;left:5px;top:3.5px;border-left:5px solid var(--white);border-top:3.5px solid transparent;border-bottom:3.5px solid transparent}

.site-foot{position:absolute;left:0;right:0;bottom:0;height:150px}
.foot-wave{position:absolute;top:0;left:0;width:100%;height:52px}
.foot-body{position:absolute;top:50px;left:0;right:0;bottom:0;background:var(--navy);text-align:center;color:var(--white)}
.foot-name{font-size:8px;font-weight:600;color:var(--gold);margin-top:16px}
.foot-nav{display:flex;justify-content:center;gap:20px;font-size:3.4px;margin-top:8px}
.socials{display:flex;justify-content:center;gap:2px;margin-top:6px}
.socials i{width:8px;height:8px;border-radius:50%;border:.6px solid var(--white)}
.copy{font-size:3.4px;margin-top:8px}
.copy b{color:var(--gold);font-weight:400}
.pgno{position:absolute;right:12px;bottom:6px;font-size:3.4px}

.product-name{font-size:3.8px;color:var(--ink);margin-top:3px}
.price{font-size:5px;font-weight:600;color:var(--ink)}
.price.gold{color:var(--gold)}
.cart-row{position:absolute;left:31px;width:170px;height:30px}
</style>
</head>
<body>

<svg width="0" height="0" style="position:absolute" aria-hidden="true">
  <defs>
    <symbol id="hero-wave" viewBox="0 0 337 56" preserveAspectRatio="none">
      <path d="M0 56 V34 C60 14 120 22 170 36 C230 52 290 46 337 20 V56Z" fill="#ffffff"/>
      <path d="M0 30 C60 8 120 18 170 32 C230 48 290 42 337 14" fill="none" stroke="#2f2d62" stroke-width="4"/>
    </symbol>
    <symbol id="foot-wave" viewBox="0 0 337 52" preserveAspectRatio="none">
      <path d="M0 52 V30 C70 16 120 40 190 36 C260 32 300 12 337 4 V52Z" fill="#2f2d62"/>
      <path d="M60 30 C140 40 230 26 337 10" fill="none" stroke="#c8b66a" stroke-width="3"/>
    </symbol>
  </defs>
</svg>

<!-- ============ HOME ============ -->
<section class="page col-a" style="top:40px;height:1132px">
  <div class="topbar">Call Us : +1 555 010 0199 &nbsp;|&nbsp; Email : info@harmonaura.example</div>
  <nav class="nav"><span>EVENTS</span><span>ABOUT</span><span>SYNERGISE</span><span>WISDOM</span><span>SHOP</span></nav>
  <div class="brand"><span class="brand-name">Harmonaura</span></div>

  <div class="hero" style="height:206px">
    <div class="ph" role="img" aria-label="Clear blue water surface with sunlight ripples" style="background:linear-gradient(180deg,#1a6fae 0%,#2aa3d8 50%,#6fd3ea 100%)"></div>
    <h1 style="top:48px">Harmonaura</h1>
    <p class="abs center" style="top:82px;left:60px;right:60px;font-size:4.6px;line-height:7px;color:#fff">Sed ut perspiciatis unde omnis iste natus error sit volup totam accusantium doloremque laudantium</p>
    <div class="abs center" style="top:110px;left:0;right:0"><span class="btn navy">READ MORE</span></div>
    <svg class="wave"><use href="#hero-wave"/></svg>
  </div>

  <div class="abs round ring" role="img" aria-label="Person meditating on a rock at sunset" style="left:35px;top:245px;width:118px;height:118px;background:radial-gradient(circle at 50% 40%,#f3c56a,#b0652a 55%,#3d2a22)"></div>
  <div class="abs" style="left:182px;top:260px;width:125px">
    <h2 class="title left">SAY HARMONAURA</h2>
    <p class="txt" style="margin-top:4px">Sed ut perspiciatis unde omnis iste natus error sit voluptatem accusantium doloremque laudantium, totam rem aperiam, eaque ipsa quae ab illo inventore veritatis et quasi architecto beatae vitae dicta sunt explicabo. Nemo enim ipsam voluptatem quia voluptas sit aspernatur aut odit aut fugit, sed quia consequuntur magni dolores eos qui ratione voluptatem sequi nesciunt. Neque porro quisquam est, qui dolorem ipsum quia dolor sit amet, consectetur, adipisci velit, sed quia non numquam eius modi tempora incidunt ut labore et dolore magnam aliquam quaerat voluptatem.</p>
    <div style="margin-top:6px"><span class="btn navy">Read More</span></div>
  </div>

  <div class="sec" style="top:398px;height:262px;background:radial-gradient(ellipse at 50% 50%,#fbf8ee,#efe6c8)">
    <svg class="abs" style="left:0;bottom:-2px;width:100%;height:16px" viewBox="0 0 337 16" preserveAspectRatio="none"><path d="M0 2 C110 18 227 18 337 2" fill="none" stroke="#2f2d62" stroke-width="2"/></svg>
    <h2 class="title" style="margin-top:32px">SYNERGY</h2>
    <div class="card" style="left:32px;top:57px;width:133px;height:165px">
      <div role="img" aria-label="Woman meditating in a calm room" style="height:85px;background:linear-gradient(135deg,#d7d2c8,#8e7a68 60%,#3f3a3a)"></div>
      <p style="font-size:6px;font-weight:500;margin-top:7px">Pathways</p>
      <p class="txt" style="margin:3px 10px 0">Sed ut perspiciatis unde omnis iste natus error sit voluptatem accusantium doloremque laudantium, totam rem aperiam, eaque ipsa quae ab illo inventore veritatis et quasi architecto beatae vitae dicta sunt explicabo.</p>
      <div style="margin-top:6px"><span class="btn">Learn More</span></div>
    </div>
    <div class="card" style="left:173px;top:57px;width:133px;height:165px">
      <div role="img" aria-label="Singing bowls on a person lying on colourful cloth" style="height:85px;background:linear-gradient(135deg,#c9a35a,#4d5b8c 55%,#8a3a3a)"></div>
      <p style="font-size:6px;font-weight:500;margin-top:7px">Energies</p>
      <p class="txt" style="margin:3px 10px 0">Sed ut perspiciatis unde omnis iste natus error sit voluptatem accusantium doloremque laudantium, totam rem aperiam, eaque ipsa quae ab illo inventore veritatis et quasi architecto beatae vitae dicta sunt explicabo.</p>
      <div style="margin-top:6px"><span class="btn">Learn More</span></div>
    </div>
  </div>

  <h2 class="title abs" style="top:687px;left:0;right:0">SYNCHRONISE</h2>
  <div class="abs" role="img" aria-label="Hands playing a singing bowl with candles" style="left:37px;top:712px;width:98px;height:103px;border-radius:6px;background:linear-gradient(135deg,#c7b9a6,#8b6a4a 55%,#3b2e28)"></div>
  <div class="abs" style="left:178px;top:716px;width:125px">
    <p class="head-sm">SED UT PERSPICIATIS UNDE OMNIS ISTE NATUS ERROR SIT VOLUPTATEM</p>
    <p class="date">22 AUGUST 2022</p>
    <p class="txt">Nemo enim ipsam voluptatem quia voluptas sit aspernatur aut odit aut fugit, sed quia consequuntur magni dolores eos qui ratione voluptatem sequi nesciunt. Neque porro quisquam est, qui dolorem ipsum quia dolor sit amet, consectetur, adipisci velit, sed quia non numquam eius modi tempora incidunt ut labore et dolore magnam aliquam quaerat voluptatem.</p>
    <p class="link">Book My Space →</p>
  </div>
  <div class="abs center" style="top:830px;left:0;right:0"><span class="btn">More Events</span></div>

  <div class="sec" role="img" aria-label="Person meditating on a cliff at sunset with birds" style="top:858px;height:230px;background:linear-gradient(160deg,#3e4258 0%,#a46a3e 45%,#e9a34a 65%,#5a3a2a 100%)">
  </div>
  <div class="abs" style="left:170px;top:888px;width:135px">
    <h2 class="title left light">SYNCHRONY</h2>
    <p class="txt light" style="margin-top:3px">Sed ut perspiciatis unde omnis iste natus error sit voluptatem accusantium doloremque laudantium, totam rem aperiam, eaque ipsa quae ab illo inventore veritatis et quasi architecto beatae vitae dicta sunt explicabo. Nemo enim ipsam voluptatem quia voluptas sit aspernatur aut odit aut fugit.</p>
    <div style="margin-top:6px"><span class="btn navy">Read More</span></div>
  </div>

  <footer class="site-foot">
    <svg class="foot-wave"><use href="#foot-wave"/></svg>
    <div class="foot-body">
      <p class="foot-name">Harmonaura</p>
      <nav class="foot-nav"><span>EVENTS</span><span>ABOUT</span><span>SYNERGISE</span><span>WISDOM</span><span>SHOP</span></nav>
      <div class="socials"><i></i><i></i><i></i><i></i><i></i></div>
      <p class="copy">© Copyright 2022 <b>Harmonaura</b>.All Rights Reserved</p>
      <span class="pgno">C2</span>
    </div>
  </footer>
</section>

<!-- ============ SYNERGISE ============ -->
<section class="page col-a" style="top:1210px;height:1307px">
  <div class="topbar">Call Us : +1 555 010 0199 &nbsp;|&nbsp; Email : info@harmonaura.example</div>
  <nav class="nav"><span>EVENTS</span><span>ABOUT</span><span>SYNERGISE</span><span>WISDOM</span><span>SHOP</span></nav>
  <div class="brand"><span class="brand-name">Harmonaura</span></div>

  <div class="hero" style="height:142px">
    <div class="ph" role="img" aria-label="Forest river with reflections" style="background:linear-gradient(180deg,#6b7b84 0%,#2f4a3a 45%,#1e2f26 100%)"></div>
    <h1 style="top:48px">SYNERGISE</h1>
    <svg class="wave"><use href="#hero-wave"/></svg>
  </div>

  <h2 class="title abs" style="top:198px;left:0;right:0;font-size:7px">ACHIEVING VIBRATIONAL EQUILIBRIUM</h2>

  <div class="frame" style="left:32px;top:222px;width:133px;height:168px">
    <div role="img" aria-label="Meditating figure with glowing chakra colours" style="height:85px;background:linear-gradient(180deg,#c06ad0,#5a8fd8 50%,#f2c16a)"></div>
    <p style="font-size:5.5px;font-weight:500;margin-top:7px">Chakras/Energy System</p>
    <p class="txt" style="margin:3px 6px 0">Sed ut perspiciatis unde omnis iste natus error sit voluptatem accusantium doloremque laudantium, totam rem aperiam, eaque ipsa quae ab illo inventore veritatis et quasi.</p>
    <div style="margin-top:5px"><span class="btn">Book an Event</span></div>
  </div>
  <div class="frame" style="left:173px;top:222px;width:133px;height:168px">
    <div role="img" aria-label="Deer in an autumn forest" style="height:85px;background:linear-gradient(180deg,#4a4a44,#a06a3a 60%,#3a2e22)"></div>
    <p style="font-size:5.5px;font-weight:500;margin-top:7px">Animal Energy</p>
    <p class="txt" style="margin:3px 6px 0">Sed ut perspiciatis unde omnis iste natus error sit voluptatem accusantium doloremque laudantium, totam rem aperiam, eaque ipsa quae ab illo inventore veritatis et quasi.</p>
    <div style="margin-top:5px"><span class="btn">Book an Event</span></div>
  </div>
  <div class="frame" style="left:32px;top:403px;width:133px;height:168px">
    <div role="img" aria-label="Industrial plant lit at dusk" style="height:85px;background:linear-gradient(180deg,#3b5b9a,#d98a4a 60%,#2a2a3a)"></div>
    <p style="font-size:5.5px;font-weight:500;margin-top:7px">Plant Energy System</p>
    <p class="txt" style="margin:3px 6px 0">Sed ut perspiciatis unde omnis iste natus error sit voluptatem accusantium doloremque laudantium, totam rem aperiam, eaque ipsa quae ab illo inventore veritatis et quasi.</p>
    <div style="margin-top:5px"><span class="btn">Visitation</span></div>
  </div>
  <div class="frame" style="left:173px;top:403px;width:133px;height:168px">
    <div role="img" aria-label="Hands playing traditional instruments" style="height:85px;background:linear-gradient(135deg,#6a3a2a,#c29a5a 50%,#3a2a22)"></div>
    <p style="font-size:5.5px;font-weight:500;margin-top:7px">Native Musical Instruments</p>
    <p class="txt" style="margin:3px 6px 0">Sed ut perspiciatis unde omnis iste natus error sit voluptatem accusantium doloremque laudantium, totam rem aperiam, eaque ipsa quae ab illo inventore veritatis et quasi architecto beatae vitae dicta sunt explicabo nemo enim.</p>
  </div>

  <div class="sec" style="top:595px;height:158px;background:var(--mist)">
    <h2 class="title" style="margin-top:23px">ARTICLES VIDEO</h2>
    <div class="abs" role="img" aria-label="Candle and singing bowl video still" style="left:31px;top:45px;width:89px;height:65px;background:linear-gradient(135deg,#3a2e34,#b0703a 60%,#2a2430)"><span class="play"></span></div>
    <div class="abs" role="img" aria-label="Person meditating at a lake at dusk video still" style="left:125px;top:45px;width:87px;height:65px;background:linear-gradient(180deg,#7a8aa0,#d9a56a 60%,#3a3a44)"><span class="play"></span></div>
    <div class="abs" role="img" aria-label="Hands over tarot cards video still" style="left:217px;top:45px;width:88px;height:65px;background:linear-gradient(135deg,#4a3a6a,#8a5a4a 55%,#2a2a3a)"><span class="play"></span></div>
    <div class="abs txt" style="left:31px;top:114px;width:89px;color:var(--ink)"><b style="font-weight:600">5 week ago</b><br>Sed ut perspiciatis unde omnis iste natus error sit voluptatem</div>
    <div class="abs txt" style="left:125px;top:114px;width:87px;color:var(--ink)"><b style="font-weight:600">5 week ago</b><br>Sed ut perspiciatis unde omnis iste natus error sit voluptatem</div>
    <div class="abs txt" style="left:217px;top:114px;width:88px;color:var(--ink)"><b style="font-weight:600">5 week ago</b><br>Sed ut perspiciatis unde omnis iste natus error sit voluptatem</div>
  </div>

  <div class="sec" style="top:753px;height:138px;background:var(--gold)">
    <h2 class="title" style="margin-top:22px;font-size:7px">TESTIMONIALS</h2>
    <div class="abs round" role="img" aria-label="Portrait of a client" style="left:153px;top:36px;width:30px;height:30px;background:linear-gradient(135deg,#e8cdb0,#9a6a4a);border:1.5px solid #fff"></div>
    <div class="abs" style="left:35px;top:80px;width:10px;height:10px;border:.6px solid #fff;color:#fff;font-size:5px;text-align:center;line-height:9px">‹</div>
    <div class="abs" style="right:35px;top:80px;width:10px;height:10px;border:.6px solid #fff;color:#fff;font-size:5px;text-align:center;line-height:9px">›</div>
    <p class="abs txt light center" style="left:62px;right:62px;top:75px">“ Neque porro quisquam est, qui dolorem ipsum quia dolor sit amet, consectetur, adipisci velit, sed quia non numquam eius modi tempora incidunt ut labore et dolore magnam aliquam quaerat voluptatem. Ut enim ad minima veniam, quis nostrum exercitationem ullam corporis suscipit laboriosam. ”</p>
    <p class="abs center" style="left:0;right:0;top:108px;font-size:3.6px;font-weight:600;color:#fff">~ LEO MARSH</p>
  </div>

  <h2 class="title abs" style="top:912px;left:0;right:0;font-size:7px">ABOUT MEDIATION</h2>
  <div class="abs" role="img" aria-label="Bare feet walking on sand at sunset" style="left:32px;top:935px;width:153px;height:100px;background:linear-gradient(135deg,#2a2622,#b0804a 55%,#3a2a22)"><span class="play"></span></div>
  <p class="abs txt" style="left:195px;top:935px;width:111px">Sed ut perspiciatis unde omnis iste natus error sit voluptatem accusantium doloremque laudantium, totam rem aperiam, eaque ipsa quae ab illo inventore veritatis et quasi architecto beatae vitae dicta sunt explicabo. Nemo enim ipsam voluptatem quia voluptas sit aspernatur aut odit aut fugit, sed quia consequuntur magni dolores eos qui ratione voluptatem sequi nesciunt. Neque porro quisquam est, qui dolorem ipsum quia dolor sit amet, consectetur, adipisci velit, sed quia non numquam eius modi tempora incidunt ut labore et dolore magnam aliquam quaerat voluptatem. Ut enim ad minima veniam, quis nostrum exercitationem ullam corporis suscipit laboriosam, nisi ut aliquid ex ea commodi consequatur.</p>

  <div class="sec" role="img" aria-label="Hands holding a glowing planet in violet light" style="top:1055px;height:215px;background:radial-gradient(ellipse at 50% 40%,#7a6aa8,#3a3266 55%,#1e1a36)"></div>
  <p class="abs center" style="left:30px;right:30px;top:1105px;font-size:5.6px;line-height:12px;font-weight:500;color:#fff">SED UT PERSPICIATIS UNDE OMNIS ISTE<br>NATUS ERROR SIT VOLUPTATEM ACCUSANTIUM DOLOREM</p>

  <footer class="site-foot">
    <svg class="foot-wave"><use href="#foot-wave"/></svg>
    <div class="foot-body">
      <p class="foot-name">Harmonaura</p>
      <nav class="foot-nav"><span>EVENTS</span><span>ABOUT</span><span>SYNERGISE</span><span>WISDOM</span><span>SHOP</span></nav>
      <div class="socials"><i></i><i></i><i></i><i></i><i></i></div>
      <p class="copy">© Copyright 2022 <b>Harmonaura</b>.All Rights Reserved</p>
      <span class="pgno">C2</span>
    </div>
  </footer>
</section>

<!-- ============ EVENTS ============ -->
<section class="page col-b" style="top:42px;height:841px">
  <div class="topbar">Call Us : +1 555 010 0199 &nbsp;|&nbsp; Email : info@harmonaura.example</div>
  <nav class="nav"><span>EVENTS</span><span>ABOUT</span><span>SYNERGISE</span><span>WISDOM</span><span>SHOP</span></nav>
  <div class="brand"><span class="brand-name">Harmonaura</span></div>

  <div class="hero" style="height:166px">
    <div class="ph" role="img" aria-label="Woman walking on a misty beach at sunrise" style="background:linear-gradient(180deg,#5d5852 0%,#b7a78e 45%,#8a7d6c 100%)"></div>
    <h1 style="top:36px">Events</h1>
    <svg class="wave"><use href="#hero-wave"/></svg>
  </div>

  <h2 class="title abs" style="top:198px;left:0;right:0">UPCOMING EVENT</h2>
  <div class="abs" role="img" aria-label="Singing bowl ceremony with candles" style="left:37px;top:225px;width:125px;height:103px;border-radius:6px;background:linear-gradient(135deg,#c7b9a6,#8b6a4a 55%,#3b2e28)"></div>
  <div class="abs" style="left:177px;top:229px;width:125px">
    <p class="head-sm">SED UT PERSPICIATIS UNDE OMNIS ISTE NATUS ERROR SIT VOLUPTATEM</p>
    <p class="date">22 AUGUST 2022</p>
    <p class="txt">Nemo enim ipsam voluptatem quia voluptas sit aspernatur aut odit aut fugit, sed quia consequuntur magni dolores eos qui ratione voluptatem sequi nesciunt. Neque porro quisquam est, qui dolorem ipsum quia dolor sit amet, consectetur, adipisci velit, sed quia non numquam eius modi tempora incidunt ut labore et dolore magnam aliquam quaerat voluptatem.</p>
    <p class="link">Book My Space →</p>
  </div>

  <div class="card" style="left:31px;top:358px;width:82px;height:110px">
    <div role="img" aria-label="Person meditating on a mountain at dusk" style="height:62px;background:linear-gradient(180deg,#d9b07a,#7a5a4a 60%,#2a2a2a)"></div>
    <p style="font-size:3.8px;margin-top:4px">04 August 2022</p>
    <p class="txt" style="margin:2px 5px 0">Sed ut perspiciatis unde omnis iste natus error sit voluptatem accusantium</p>
    <p class="link" style="margin-top:3px">Read More →</p>
  </div>
  <div class="card" style="left:127px;top:358px;width:82px;height:110px">
    <div role="img" aria-label="Woman playing a gong" style="height:62px;background:linear-gradient(135deg,#8a3a2a,#d9a86a 50%,#f2e4d2)"></div>
    <p style="font-size:3.8px;margin-top:4px">04 August 2022</p>
    <p class="txt" style="margin:2px 5px 0">Sed ut perspiciatis unde omnis iste natus error sit voluptatem accusantium</p>
    <p class="link" style="margin-top:3px">Read More →</p>
  </div>
  <div class="card" style="left:223px;top:358px;width:82px;height:110px">
    <div role="img" aria-label="Praying hands against the sky" style="height:62px;background:linear-gradient(180deg,#4a6a9a,#e2a86a 60%,#2a2a3a)"></div>
    <p style="font-size:3.8px;margin-top:4px">04 August 2022</p>
    <p class="txt" style="margin:2px 5px 0">Sed ut perspiciatis unde omnis iste natus error sit voluptatem accusantium</p>
    <p class="link" style="margin-top:3px">Read More →</p>
  </div>
  <div class="abs center" style="top:479px;left:0;right:0"><span class="btn">Click For More Info</span></div>

  <h2 class="title abs" style="top:524px;left:0;right:0">PHOTO GALLERY</h2>
  <div class="abs" role="img" aria-label="Singing bowl with candles" style="left:31px;top:545px;width:89px;height:65px;background:linear-gradient(135deg,#3a2a2a,#a86a3a 60%,#6a2a2a)"></div>
  <div class="abs" role="img" aria-label="Sound bath with bowls" style="left:125px;top:545px;width:87px;height:65px;background:linear-gradient(135deg,#6a7a8a,#c9a56a 55%,#3a4a5a)"></div>
  <div class="abs" role="img" aria-label="Golden bowls with flowers" style="left:217px;top:545px;width:88px;height:65px;background:linear-gradient(135deg,#d9c08a,#8a6a3a 60%,#3a2a1a)"></div>
  <div class="abs" role="img" aria-label="Group meditating on mats" style="left:31px;top:616px;width:89px;height:65px;background:linear-gradient(135deg,#8a9aa8,#4a5a6a 60%,#2a3038)"></div>
  <div class="abs" role="img" aria-label="Woman meditating by plants" style="left:125px;top:616px;width:87px;height:65px;background:linear-gradient(135deg,#d8d8d2,#6a7a5a 55%,#2a2a2a)"></div>
  <div class="abs" role="img" aria-label="Hand reaching toward the sunset" style="left:217px;top:616px;width:88px;height:65px;background:linear-gradient(180deg,#3a4a6a,#e2a04a 60%,#2a1e1a)"></div>

  <footer class="site-foot">
    <svg class="foot-wave"><use href="#foot-wave"/></svg>
    <div class="foot-body">
      <p class="foot-name">Harmonaura</p>
      <nav class="foot-nav"><span>EVENTS</span><span>ABOUT</span><span>SYNERGISE</span><span>WISDOM</span><span>SHOP</span></nav>
      <div class="socials"><i></i><i></i><i></i><i></i><i></i></div>
      <p class="copy">© Copyright 2022 <b>Harmonaura</b>.All Rights Reserved</p>
      <span class="pgno">C2</span>
    </div>
  </footer>
</section>

<!-- ============ INSPIRATIONAL MESSAGES ============ -->
<section class="page col-b" style="top:915px;height:965px">
  <div class="topbar">Call Us : +1 555 010 0199 &nbsp;|&nbsp; Email : info@harmonaura.example</div>
  <nav class="nav"><span>EVENTS</span><span>ABOUT</span><span>SYNERGISE</span><span>WISDOM</span><span>SHOP</span></nav>
  <div class="brand"><span class="brand-name">Harmonaura</span></div>

  <div class="hero" style="height:144px">
    <div class="ph" role="img" aria-label="Hands raised toward birds in a golden sky" style="background:linear-gradient(180deg,#4a4034 0%,#a67c4a 50%,#6a4e32 100%)"></div>
    <h1 style="top:48px;font-size:14px">INSPIRATIONAL MESSAGES</h1>
    <svg class="wave"><use href="#hero-wave"/></svg>
  </div>

  <h2 class="title abs" style="top:198px;left:0;right:0">FEATURE ARTICLE</h2>
  <div class="abs" role="img" aria-label="Woman meditating beside a plant" style="left:37px;top:225px;width:125px;height:107px;border-radius:6px;background:linear-gradient(135deg,#dcdad2,#6a7a5a 55%,#2a2a2a)"></div>
  <div class="abs" style="left:177px;top:229px;width:125px">
    <p class="head-sm">SED UT PERSPICIATIS UNDE OMNIS ISTE NATUS ERROR SIT VOLUPTATEM</p>
    <p class="date">22 AUGUST 2022</p>
    <p class="txt">Nemo enim ipsam voluptatem quia voluptas sit aspernatur aut odit aut fugit, sed quia consequuntur magni dolores eos qui ratione voluptatem sequi nesciunt. Neque porro quisquam est, qui dolorem ipsum quia dolor sit amet, consectetur, adipisci velit, sed quia non numquam eius modi tempora incidunt.</p>
    <div style="margin-top:5px"><span class="btn">More Articles</span></div>
  </div>

  <div class="sec" role="img" aria-label="Man standing on a pillar above misty mountains" style="top:355px;height:170px;background:linear-gradient(180deg,#cfe2ee 0%,#a9c6da 50%,#6f8aa0 100%)"></div>
  <h2 class="title abs" style="top:378px;left:0;right:0">WISDOM</h2>
  <p class="abs txt center" style="top:392px;left:65px;right:65px;color:#5a5a66">Sed ut perspiciatis unde omnis iste natus error sit voluptatem accusantium doloremque laudantium, totam rem aperiam, eaque ipsa quae ab illo inventore veritatis et quasi architecto beatae vitae dicta sunt explicabo. Nemo enim ipsam voluptatem quia voluptas sit aspernatur aut odit aut fugit, sed quia conse.</p>

  <h2 class="title abs" style="top:548px;left:0;right:0">INTERVIEWS</h2>
  <div class="abs" role="img" aria-label="Woman beside a gong, video still" style="left:31px;top:570px;width:89px;height:38px;background:linear-gradient(135deg,#8a3a2a,#d9a86a 55%,#f0e2d0)"><span class="play"></span></div>
  <div class="abs" role="img" aria-label="Woman meditating indoors, video still" style="left:125px;top:570px;width:87px;height:38px;background:linear-gradient(135deg,#5a5a5a,#c9c9c2 55%,#3a3a3a)"><span class="play"></span></div>
  <div class="abs" role="img" aria-label="Woman on an exercise ball, video still" style="left:217px;top:570px;width:88px;height:38px;background:linear-gradient(135deg,#e2e2dc,#9a9a92 55%,#5a5a5a)"><span class="play"></span></div>
  <div class="abs center" style="top:645px;left:0;right:0"><span class="btn">More Interviews</span></div>

  <div class="abs round" role="img" aria-label="Smiling woman with hands together" style="left:35px;top:688px;width:127px;height:127px;background:radial-gradient(circle at 50% 40%,#f2ddc4,#c9a07a 55%,#8a6a52)"></div>
  <div class="abs" style="left:172px;top:692px;width:132px">
    <h2 class="title left">TESTIMONIALS</h2>
    <p class="txt" style="margin-top:4px">“ Sed ut perspiciatis unde omnis iste natus error sit voluptatem accusantium doloremque laudantium, totam rem aperiam, eaque ipsa quae ab illo inventore veritatis et quasi architecto beatae vitae dicta sunt explicabo. Nemo enim ipsam voluptatem quia voluptas sit aspernatur aut odit aut fugit, sed quia consequuntur magni dolores eos qui ratione voluptatem sequi nesciunt. Neque porro quisquam est, qui dolorem ipsum quia dolor sit amet. ”</p>
    <p style="font-size:3.8px;font-weight:600;margin-top:4px">~Leo Marsh</p>
    <p class="txt">Sed ut perspiciatis unde</p>
  </div>

  <footer class="site-foot">
    <svg class="foot-wave"><use href="#foot-wave"/></svg>
    <div class="foot-body">
      <p class="foot-name">Harmonaura</p>
      <nav class="foot-nav"><span>EVENTS</span><span>ABOUT</span><span>SYNERGISE</span><span>WISDOM</span><span>SHOP</span></nav>
      <div class="socials"><i></i><i></i><i></i><i></i><i></i></div>
      <p class="copy">© Copyright 2022 <b>Harmonaura</b>.All Rights Reserved</p>
      <span class="pgno">C2</span>
    </div>
  </footer>
</section>

<!-- ============ MALAS ============ -->
<section class="page col-b" style="top:1903px;height:497px">
  <div class="topbar">Call Us : +1 555 010 0199 &nbsp;|&nbsp; Email : info@harmonaura.example</div>
  <nav class="nav"><span>EVENTS</span><span>ABOUT</span><span>SYNERGISE</span><span>WISDOM</span><span>SHOP</span></nav>
  <div class="brand"><span class="brand-name">Harmonaura</span></div>

  <div class="hero" style="height:148px">
    <div class="ph" role="img" aria-label="Mala bead necklace resting on a stone" style="background:linear-gradient(180deg,#8a969a 0%,#6a625a 50%,#a89a88 100%)"></div>
    <h1 style="top:36px">MALAS</h1>
    <svg class="wave"><use href="#hero-wave"/></svg>
  </div>

  <div class="frame" style="left:31px;top:200px;width:87px;height:126px;border-color:#e3e3e8">
    <div role="img" aria-label="Amber bead mala" style="height:62px;background:linear-gradient(135deg,#f2e6d2,#d98a3a 55%,#8a4a1a)"></div>
    <p class="price gold" style="margin-top:4px">$25.99</p>
    <p class="head-sm" style="font-size:4px;line-height:5.4px">Sed ut perspiciatis unde omnis iste natus</p>
    <div style="margin-top:5px"><span class="btn line">Add To Cart</span></div>
  </div>
  <div class="frame" style="left:124px;top:200px;width:87px;height:126px;border-color:#e3e3e8">
    <div role="img" aria-label="Wooden bead mala on linen" style="height:62px;background:linear-gradient(135deg,#6a7a9a,#b86a3a 55%,#5a3a2a)"></div>
    <p class="price gold" style="margin-top:4px">$25.99</p>
    <p class="head-sm" style="font-size:4px;line-height:5.4px">Sed ut perspiciatis unde omnis iste natus</p>
    <div style="margin-top:5px"><span class="btn line">Add To Cart</span></div>
  </div>
  <div class="frame" style="left:217px;top:200px;width:87px;height:126px;border-color:#e3e3e8">
    <div role="img" aria-label="Dark red bead mala" style="height:62px;background:linear-gradient(135deg,#e2dcd8,#7a2a3a 55%,#3a1a22)"></div>
    <p class="price gold" style="margin-top:4px">$25.99</p>
    <p class="head-sm" style="font-size:4px;line-height:5.4px">Sed ut perspiciatis unde omnis iste natus</p>
    <div style="margin-top:5px"><span class="btn line">Add To Cart</span></div>
  </div>

  <footer class="site-foot">
    <svg class="foot-wave"><use href="#foot-wave"/></svg>
    <div class="foot-body">
      <p class="foot-name">Harmonaura</p>
      <nav class="foot-nav"><span>EVENTS</span><span>ABOUT</span><span>SYNERGISE</span><span>WISDOM</span><span>SHOP</span></nav>
      <div class="socials"><i></i><i></i><i></i><i></i><i></i></div>
      <p class="copy">© Copyright 2022 <b>Harmonaura</b>.All Rights Reserved</p>
      <span class="pgno">C2</span>
    </div>
  </footer>
</section>

<!-- ============ ABOUT ============ -->
<section class="page col-c" style="top:42px;height:1118px">
  <div class="topbar">Call Us : +1 555 010 0199 &nbsp;|&nbsp; Email : info@harmonaura.example</div>
  <nav class="nav"><span>EVENTS</span><span>ABOUT</span><span>SYNERGISE</span><span>WISDOM</span><span>SHOP</span></nav>
  <div class="brand"><span class="brand-name">Harmonaura</span></div>

  <div class="hero" style="height:146px">
    <div class="ph" role="img" aria-label="Sound healing session with a singing bowl" style="background:linear-gradient(135deg,#5a2a1a 0%,#c98a4a 45%,#7a3d22 100%)"></div>
    <h1 style="top:50px">ABOUT US</h1>
    <svg class="wave"><use href="#hero-wave"/></svg>
  </div>

  <div class="abs round ring-gold" role="img" aria-label="Portrait of Clara Vale" style="left:45px;top:195px;width:112px;height:112px;background:radial-gradient(circle at 50% 40%,#e8c9a6,#a87a4a 55%,#d9c06a)"></div>
  <div class="abs" style="left:173px;top:204px;width:132px">
    <h2 class="title left">ABOUT CLARA VALE</h2>
    <p class="txt" style="margin-top:4px">Sed ut perspiciatis unde omnis iste natus error sit voluptatem accusantium doloremque laudantium, totam rem aperiam, eaque ipsa quae ab illo inventore veritatis et quasi architecto beatae vitae dicta sunt explicabo. Nemo enim ipsam voluptatem quia voluptas sit aspernatur aut odit aut fugit, sed quia consequuntur magni dolores eos qui ratione voluptatem sequi nesciunt. Neque porro quisquam est, qui dolorem ipsum quia dolor sit amet, consectetur, adipisci velit, sed quia non numquam eius modi tempora incidunt.</p>
  </div>

  <div class="abs" style="left:45px;top:340px;width:128px">
    <h2 class="title left">ABOUT RUTH ASHBY</h2>
    <p class="txt" style="margin-top:4px">Sed ut perspiciatis unde omnis iste natus error sit voluptatem accusantium doloremque laudantium, totam rem aperiam, eaque ipsa quae ab illo inventore veritatis et quasi architecto beatae vitae dicta sunt explicabo. Nemo enim ipsam voluptatem quia voluptas sit aspernatur aut odit aut fugit, sed quia consequuntur magni dolores eos qui ratione voluptatem sequi nesciunt. Neque porro quisquam est, qui dolorem ipsum quia dolor sit amet, consectetur, adipisci velit, sed quia non numquam eius modi tempora incidunt.</p>
  </div>
  <div class="abs round ring-gold" role="img" aria-label="Portrait of Ruth Ashby" style="left:180px;top:328px;width:112px;height:112px;background:radial-gradient(circle at 50% 40%,#f0e6dc,#c9b8a8 55%,#8a7a6a)"></div>

  <div class="sec" style="top:460px;height:158px;background:var(--mist)">
    <div class="abs" role="img" aria-label="Smiling woman with hand on heart" style="left:0;top:0;width:160px;height:158px;background:linear-gradient(135deg,#8a7a6a,#e2c2b0 50%,#c9a090)"></div>
    <div class="abs" style="left:175px;top:28px;width:130px">
      <h2 class="title left">TESTIMONIALS</h2>
      <p class="txt" style="margin-top:4px">“ Sed ut perspiciatis unde omnis iste natus error sit voluptatem accusantium doloremque laudantium, totam rem aperiam, eaque ipsa quae ab illo inventore veritatis et quasi architecto beatae vitae dicta sunt explicabo. Nemo enim ipsam voluptatem quia voluptas sit aspernatur aut odit aut fugit, sed quia consequuntur magni dolores eos qui ratione voluptatem sequi nesciunt. ”</p>
      <p style="font-size:3.8px;font-weight:600;margin-top:4px">~Leo Marsh</p>
      <p class="txt">Sed ut perspiciatis unde</p>
    </div>
  </div>

  <h2 class="title abs" style="top:630px;left:0;right:0">OUR VIDEO</h2>
  <div class="abs" role="img" aria-label="Group meditating in a warm candlelit studio, video still" style="left:66px;top:655px;width:204px;height:113px;background:linear-gradient(135deg,#3a2218,#b0683a 50%,#5a3022)"><span class="play" style="width:20px;height:20px;margin:-10px 0 0 -10px"></span></div>

  <h2 class="title abs" style="top:802px;left:0;right:0">PHOTO GALLERY</h2>
  <div class="abs" role="img" aria-label="Singing bowl with candles" style="left:31px;top:821px;width:89px;height:64px;background:linear-gradient(135deg,#3a2a2a,#a86a3a 60%,#6a2a2a)"></div>
  <div class="abs" role="img" aria-label="Sound bath with bowls" style="left:125px;top:821px;width:87px;height:64px;background:linear-gradient(135deg,#6a7a8a,#c9a56a 55%,#3a4a5a)"></div>
  <div class="abs" role="img" aria-label="Golden bowls with flowers" style="left:217px;top:821px;width:88px;height:64px;background:linear-gradient(135deg,#d9c08a,#8a6a3a 60%,#3a2a1a)"></div>
  <div class="abs" role="img" aria-label="Group meditating on mats" style="left:31px;top:892px;width:89px;height:64px;background:linear-gradient(135deg,#8a9aa8,#4a5a6a 60%,#2a3038)"></div>
  <div class="abs" role="img" aria-label="Woman meditating by plants" style="left:125px;top:892px;width:87px;height:64px;background:linear-gradient(135deg,#d8d8d2,#6a7a5a 55%,#2a2a2a)"></div>
  <div class="abs" role="img" aria-label="Hand reaching toward the sunset" style="left:217px;top:892px;width:88px;height:64px;background:linear-gradient(180deg,#3a4a6a,#e2a04a 60%,#2a1e1a)"></div>

  <footer class="site-foot">
    <svg class="foot-wave"><use href="#foot-wave"/></svg>
    <div class="foot-body">
      <p class="foot-name">Harmonaura</p>
      <nav class="foot-nav"><span>EVENTS</span><span>ABOUT</span><span>SYNERGISE</span><span>WISDOM</span><span>SHOP</span></nav>
      <div class="socials"><i></i><i></i><i></i><i></i><i></i></div>
      <p class="copy">© Copyright 2022 <b>Harmonaura</b>.All Rights Reserved</p>
      <span class="pgno">C2</span>
    </div>
  </footer>
</section>

<!-- ============ SHOP ============ -->
<section class="page col-c" style="top:1185px;height:643px">
  <div class="topbar">Call Us : +1 555 010 0199 &nbsp;|&nbsp; Email : info@harmonaura.example</div>
  <nav class="nav"><span>EVENTS</span><span>ABOUT</span><span>SYNERGISE</span><span>WISDOM</span><span>SHOP</span></nav>
  <div class="brand"><span class="brand-name">Harmonaura</span></div>

  <div class="hero" style="height:140px">
    <div class="ph" role="img" aria-label="Hands holding dark prayer beads" style="background:linear-gradient(135deg,#2a2222 0%,#6a4a3a 50%,#1e1818 100%)"></div>
    <h1 style="top:44px">SHOP</h1>
    <svg class="wave"><use href="#hero-wave"/></svg>
  </div>

  <h2 class="title abs" style="top:198px;left:0;right:0">FEATURED PRODUCTS</h2>

  <div class="abs center" style="left:31px;top:222px;width:64px">
    <div role="img" aria-label="Dark wooden bead bracelets" style="height:76px;background:linear-gradient(135deg,#5a3a4a,#2a1a22 60%,#8a6a7a)"></div>
    <p class="product-name">Product Name</p><p class="price">$25.99</p>
    <div style="margin-top:3px"><span class="btn" style="padding:2px 6px">ADD TO CART</span></div>
  </div>
  <div class="abs center" style="left:101px;top:222px;width:64px">
    <div role="img" aria-label="Colourful painted abstract art" style="height:76px;background:linear-gradient(135deg,#e25a8a,#5ac9c9 50%,#f2c05a)"></div>
    <p class="product-name">Product Name</p><p class="price">$25.99</p>
    <div style="margin-top:3px"><span class="btn" style="padding:2px 6px">ADD TO CART</span></div>
  </div>
  <div class="abs center" style="left:171px;top:222px;width:64px">
    <div role="img" aria-label="Stack of books" style="height:76px;background:linear-gradient(180deg,#f2f0ea,#c9c0b0 60%,#6a6a6a)"></div>
    <p class="product-name">Product Name</p><p class="price">$25.99</p>
    <div style="margin-top:3px"><span class="btn" style="padding:2px 6px">ADD TO CART</span></div>
  </div>
  <div class="abs center" style="left:241px;top:222px;width:64px">
    <div role="img" aria-label="Red fish in blue water art" style="height:76px;background:linear-gradient(135deg,#1a2a6a,#c93a5a 55%,#2a4a9a)"></div>
    <p class="product-name">Product Name</p><p class="price">$25.99</p>
    <div style="margin-top:3px"><span class="btn" style="padding:2px 6px">ADD TO CART</span></div>
  </div>

  <div class="abs center" style="left:31px;top:360px;width:64px">
    <div role="img" aria-label="Open books stacked" style="height:77px;background:linear-gradient(180deg,#d9c9b0,#8a3a2a 60%,#3a2a22)"></div>
    <p class="product-name">Product Name</p><p class="price">$25.99</p>
    <div style="margin-top:3px"><span class="btn" style="padding:2px 6px">ADD TO CART</span></div>
  </div>
  <div class="abs center" style="left:101px;top:360px;width:64px">
    <div role="img" aria-label="Glowing cosmic artwork" style="height:77px;background:radial-gradient(circle,#c9a0f2,#4a2a8a 50%,#120e2a)"></div>
    <p class="product-name">Product Name</p><p class="price">$25.99</p>
    <div style="margin-top:3px"><span class="btn" style="padding:2px 6px">ADD TO CART</span></div>
  </div>
  <div class="abs center" style="left:171px;top:360px;width:64px">
    <div role="img" aria-label="Colourful geometric painting" style="height:77px;background:linear-gradient(135deg,#f2d03a,#3ab0a0 50%,#e25a3a)"></div>
    <p class="product-name">Product Name</p><p class="price">$25.99</p>
    <div style="margin-top:3px"><span class="btn" style="padding:2px 6px">ADD TO CART</span></div>
  </div>
  <div class="abs center" style="left:241px;top:360px;width:64px">
    <div role="img" aria-label="Prayer beads on dark cloth" style="height:77px;background:linear-gradient(135deg,#2a2222,#6a4a3a 55%,#1a1414)"></div>
    <p class="product-name">Product Name</p><p class="price">$25.99</p>
    <div style="margin-top:3px"><span class="btn" style="padding:2px 6px">ADD TO CART</span></div>
  </div>

  <footer class="site-foot">
    <svg class="foot-wave"><use href="#foot-wave"/></svg>
    <div class="foot-body">
      <p class="foot-name">Harmonaura</p>
      <nav class="foot-nav"><span>EVENTS</span><span>ABOUT</span><span>SYNERGISE</span><span>WISDOM</span><span>SHOP</span></nav>
      <div class="socials"><i></i><i></i><i></i><i></i><i></i></div>
      <p class="copy">© Copyright 2022 <b>Harmonaura</b>.All Rights Reserved</p>
      <span class="pgno">C2</span>
    </div>
  </footer>
</section>

<!-- ============ CART ============ -->
<section class="page col-c" style="top:1843px;height:529px">
  <div class="topbar">Call Us : +1 555 010 0199 &nbsp;|&nbsp; Email : info@harmonaura.example</div>
  <nav class="nav"><span>EVENTS</span><span>ABOUT</span><span>SYNERGISE</span><span>WISDOM</span><span>SHOP</span></nav>
  <div class="brand"><span class="brand-name">Harmonaura</span></div>

  <div class="hero" style="height:142px">
    <div class="ph" role="img" aria-label="Open book under a starry blue sky" style="background:linear-gradient(180deg,#1a2a6a 0%,#3a5ab0 50%,#122052 100%)"></div>
    <h1 style="top:40px">CART</h1>
    <svg class="wave"><use href="#hero-wave"/></svg>
  </div>

  <p class="abs" style="left:31px;top:200px;font-size:4.6px;font-weight:600">Cart Items</p>
  <div class="abs" style="left:31px;top:210px;width:170px;font-size:3.2px;color:var(--muted);border-bottom:.5px solid #ddd;padding-bottom:2px">
    <span>Product</span><span style="position:absolute;left:122px">Qty</span><span style="position:absolute;left:150px">Amount</span>
  </div>

  <div class="cart-row" style="top:224px">
    <div class="abs" role="img" aria-label="Prayer beads" style="left:0;top:0;width:33px;height:28px;background:linear-gradient(135deg,#5a3a4a,#2a1a22)"></div>
    <p class="abs" style="left:39px;top:2px;width:75px;font-size:3.4px;line-height:5px">Sed ut perspiciatis unde omnis iste serror sit voluptatem</p>
    <p class="abs txt" style="left:39px;top:14px">✕ Remove Items &nbsp; ♡ Move to favorite</p>
    <p class="abs txt" style="left:122px;top:2px">‹ 1 ›</p>
    <p class="abs" style="left:150px;top:2px;font-size:3.4px">$25.99</p>
  </div>
  <div class="cart-row" style="top:266px">
    <div class="abs" role="img" aria-label="Stack of books" style="left:0;top:0;width:33px;height:28px;background:linear-gradient(180deg,#f2f0ea,#6a6a6a)"></div>
    <p class="abs" style="left:39px;top:2px;width:75px;font-size:3.4px;line-height:5px">Sed ut perspiciatis unde omnis iste serror sit voluptatem</p>
    <p class="abs txt" style="left:39px;top:14px">✕ Remove Items &nbsp; ♡ Move to favorite</p>
    <p class="abs txt" style="left:122px;top:2px">‹ 1 ›</p>
    <p class="abs" style="left:150px;top:2px;font-size:3.4px">$25.99</p>
  </div>
  <div class="cart-row" style="top:309px">
    <div class="abs" role="img" aria-label="Open books" style="left:0;top:0;width:33px;height:28px;background:linear-gradient(180deg,#d9c9b0,#8a3a2a)"></div>
    <p class="abs" style="left:39px;top:2px;width:75px;font-size:3.4px;line-height:5px">Sed ut perspiciatis unde omnis iste serror sit voluptatem</p>
    <p class="abs txt" style="left:39px;top:14px">✕ Remove Items &nbsp; ♡ Move to favorite</p>
    <p class="abs txt" style="left:122px;top:2px">‹ 1 ›</p>
    <p class="abs" style="left:150px;top:2px;font-size:3.4px">$25.99</p>
  </div>
  <div class="cart-row" style="top:351px">
    <div class="abs" role="img" aria-label="Prayer beads on dark cloth" style="left:0;top:0;width:33px;height:28px;background:linear-gradient(135deg,#2a2222,#6a4a3a)"></div>
    <p class="abs" style="left:39px;top:2px;width:75px;font-size:3.4px;line-height:5px">Sed ut perspiciatis unde omnis iste serror sit voluptatem</p>
    <p class="abs txt" style="left:39px;top:14px">✕ Remove Items &nbsp; ♡ Move to favorite</p>
    <p class="abs txt" style="left:122px;top:2px">‹ 1 ›</p>
    <p class="abs" style="left:150px;top:2px;font-size:3.4px">$25.99</p>
  </div>

  <div class="abs" style="left:208px;top:197px;width:97px;height:145px;background:var(--gold);color:#fff;padding:6px 8px">
    <p class="center" style="font-size:5px;font-weight:600">SUMMARY</p>
    <p style="font-size:3.2px;margin-top:8px">Payment Method</p>
    <div style="display:flex;gap:3px;margin-top:3px">
      <span style="flex:1;border:.6px solid #fff;border-radius:6px;font-size:3.2px;text-align:center;padding:2px 0">▭ Credit Card</span>
      <span style="flex:1;border:.6px solid #fff;border-radius:6px;font-size:3.2px;text-align:center;padding:2px 0">○ Online Pay</span>
    </div>
    <p style="font-size:3.2px;margin-top:7px">Name On Card</p>
    <p style="font-size:3.2px;border-bottom:.5px solid #fff;padding-bottom:1px">Leo Marsh</p>
    <p style="font-size:3.2px;margin-top:5px">Card Number</p>
    <p style="font-size:3.2px;border-bottom:.5px solid #fff;padding-bottom:1px">•••• &nbsp;•••• &nbsp;•••• &nbsp;3671</p>
    <div style="display:flex;justify-content:space-between;margin-top:5px;font-size:3.2px">
      <span>Expiration Date<br>MM / YYYY</span><span>CVV<br>•••</span>
    </div>
    <div class="center" style="margin-top:9px"><span class="btn navy" style="padding:3px 22px">Check Out</span></div>
  </div>

  <footer class="site-foot">
    <svg class="foot-wave"><use href="#foot-wave"/></svg>
    <div class="foot-body">
      <p class="foot-name">Harmonaura</p>
      <nav class="foot-nav"><span>EVENTS</span><span>ABOUT</span><span>SYNERGISE</span><span>WISDOM</span><span>SHOP</span></nav>
      <div class="socials"><i></i><i></i><i></i><i></i><i></i></div>
      <p class="copy">© Copyright 2022 <b>Harmonaura</b>.All Rights Reserved</p>
      <span class="pgno">C2</span>
    </div>
  </footer>
</section>

</body>
</html>
```